TRAVIM 2026 Flyer for Conference

TRAVIM needs a design for a 1-page flyer that we will hand out at an upcoming event & then later post online as a pdf. There are 3 elements which need to be on the flyer:

1) A logo. This should be prominent on the design (e.g., in the middle). The flyer should use the colors that are in that logo (e.g., for accents, design elements, and/or text; not all of these have to be used):
Dark blue: #185577
Med blue: #327C9A
Teal: #4EB1C2
Light Teal: #9EDBE6

2) The conference theme -- Oceans of Knowledge: Diving into Information Literacy -- should be at the flyer's top.

3) Finally, these six tracks should be listed below the theme and the logo (it's font size should be at least a couple sizes smaller than the size used for the theme):
- Pearls of Pedagogy: Teaching Techniques that Work
- The Depth Gauge: Measuring Instructional Impact
- Techtonic Shifts: Innovation and Educational Technology
- Captain's Log: Navigating Leadership in Library Instruction
- Swimming Together: Collaborating with Others
- The Bermuda Triangle: Exploring (Seemingly) Eternal Challenges

Font styles to use
Sans Serif

Colors
0094D4
00A9DD
6FCCEA
C7EBF8
E9F6FB

Requirements
Must have
• The 3 elements listed in the description: 1) the logo, 2) the text of the theme and 3) the text for the tracks.

```html
<!DOCTYPE html>
<html lang="en">
<head>
<meta charset="utf-8">
<title>TRAVIM 2026 — Oceans of Knowledge</title>
<link rel="stylesheet" href="https://fonts.googleapis.com/css2?family=Archivo:wght@800;900&family=Jost:wght@300;400;500&display=swap">
<style>
  :root {
    --dark-blue: #185577;
    --med-blue: #327C9A;
    --teal: #4EB1C2;
    --light-teal: #9EDBE6;
    --sea-top: #1a9a98;
    --sea-mid: #0f5c60;
    --sea-deep: #0a3f45;
    --white: #ffffff;
  }
  * { margin: 0; padding: 0; box-sizing: border-box; }
  html, body { width: 927px; height: 1200px; overflow: hidden; background: var(--sea-deep); }
  .flyer {
    position: relative;
    width: 927px;
    height: 1200px;
    overflow: hidden;
    font-family: "Jost", sans-serif;
    color: var(--white);
  }
  .sea-backdrop {
    position: absolute; inset: 0;
    background:
      radial-gradient(ellipse 70% 30% at 50% 0%, rgba(60,210,200,0.55), transparent 70%),
      linear-gradient(180deg, var(--sea-top) 0%, #137572 18%, var(--sea-mid) 42%, var(--sea-deep) 75%, #0a3a40 100%);
  }
  .theme-title {
    position: absolute; top: 70px; left: 0; width: 100%;
    text-align: center;
    font-family: "Archivo", sans-serif;
    font-weight: 900;
    font-size: 104px;
    line-height: 88px;
    letter-spacing: -3px;
    background: linear-gradient(90deg, #2a8796 15%, #5cc0c8 55%, #d2fafa 85%);
    -webkit-background-clip: text;
    background-clip: text;
    color: transparent;
    filter: drop-shadow(2px 4px 4px rgba(0,30,35,0.55));
  }
  .theme-subtitle {
    position: absolute; top: 274px; left: 0; width: 100%;
    text-align: center;
    font-weight: 500;
    font-size: 29px;
    letter-spacing: 0.5px;
  }
  .brand {
    position: absolute; top: 500px; left: 0; width: 100%;
    display: flex; justify-content: center; align-items: center; gap: 22px;
  }
  .brand-dot {
    width: 26px; height: 26px; border-radius: 50%;
    background: var(--light-teal);
  }
  .brand-name {
    font-family: "Archivo", sans-serif;
    font-weight: 900;
    font-size: 112px;
    line-height: 1;
    color: var(--light-teal);
    letter-spacing: 2px;
  }
  .brand-year {
    font-family: "Archivo", sans-serif;
    font-weight: 900;
    font-size: 112px;
    line-height: 1;
    color: var(--light-teal);
  }
  .event-details {
    position: absolute; top: 700px; left: 0; width: 100%;
    text-align: center;
    font-weight: 500;
    font-size: 26px;
    letter-spacing: 6px;
    color: var(--teal);
  }
  .tracks {
    position: absolute; top: 824px; left: 67px;
    width: 782px; height: 318px;
    display: grid;
    grid-template-columns: 272px 252px 258px;
    grid-template-rows: 156px 162px;
  }
  .track-column-bg {
    position: absolute; top: 0; bottom: 0;
    background: linear-gradient(180deg, rgba(5,40,45,0.35), rgba(5,40,45,0.5));
    box-shadow: 0 0 18px rgba(0,20,25,0.35);
  }
  .track {
    position: relative;
    text-align: center;
    padding-top: 10px;
  }
  .track-name {
    font-family: "Archivo", sans-serif;
    font-weight: 900;
    font-size: 27px;
    line-height: 24px;
    color: var(--teal);
    text-transform: uppercase;
  }
  .track-focus {
    margin-top: 14px;
    font-weight: 400;
    font-size: 19.5px;
    line-height: 20px;
    text-transform: uppercase;
  }
</style>
</head>
<body>
<main class="flyer">
  <div class="sea-backdrop" role="img" aria-label="Underwater ocean scene in deep teal tones"></div>

  <h1 class="theme-title">Oceans of<br>Knowledge</h1>
  <p class="theme-subtitle">DIVING INTO INFORMATION LITERACY</p>

  <div class="brand">
    <span class="brand-dot"></span>
    <span class="brand-name">TRAVIM</span>
    <span class="brand-year">2026</span>
  </div>
  <p class="event-details">NORFOLK, VA · MAY 7-9</p>

  <section class="tracks">
    <div class="track-column-bg" style="left:0;width:272px"></div>
    <div class="track-column-bg" style="left:272px;width:252px;opacity:.6"></div>
    <div class="track-column-bg" style="left:524px;width:258px"></div>

    <article class="track">
      <h2 class="track-name">Pearls of<br>Pedagogy</h2>
      <p class="track-focus">Teaching<br>techniques<br>that work</p>
    </article>
    <article class="track">
      <h2 class="track-name">The Depth<br>Gauge</h2>
      <p class="track-focus">Measuring<br>instructional<br>impact</p>
    </article>
    <article class="track">
      <h2 class="track-name">Techtonic<br>Shifts</h2>
      <p class="track-focus">Innovation and<br>educational<br>technology</p>
    </article>
    <article class="track">
      <h2 class="track-name">Captain's<br>Log</h2>
      <p class="track-focus">Navigating<br>leadership in<br>library<br>instruction</p>
    </article>
    <article class="track">
      <h2 class="track-name">Swimming<br>Together</h2>
      <p class="track-focus">Collaborating<br>with others</p>
    </article>
    <article class="track">
      <h2 class="track-name">The Bermuda<br>Triangle</h2>
      <p class="track-focus">Exploring<br>(seemingly) eternal<br>challenges</p>
    </article>
  </section>
</main>
</body>
</html>
```